Team Building Enquiry PDF Brochure

Lumen Burrow is a beautifully painted Glow in the Dark Mini Golf Course. Our customers put on 3D glasses while they play through 18 Holes, which makes the artwork pop out from the walls!

For this design, we want to advertise our Group Booking Package - this is for team building events (e.g., corporate events) or social groups. It will be a PDF attachment that is sent out to people enquiring about team building events.

Terms and conditions that must be included are in the attached file!

The design should be landscape orientation and 2 to 3 pages.

The design should be in line with our business theme. For inspiration please visit: https://www.lumenburrow.com.au/group-bookings/

The design should be fun and exciting with some catchy headlines and engaging text. Integrated social proof (such as mentioning previous team buildings we have hosted for companies) is also important.

For further inspiration, please find attached a copy of our Birthday Party PDF brochure. The font used is called Komika Axis.

```html
<!DOCTYPE html>
<html lang="en">
<head>
<meta charset="utf-8">
<title>Lumen Burrow – Group Bookings Brochure</title>
<link rel="stylesheet" href="https://fonts.googleapis.com/css2?family=Exo+2:ital,wght@1,700;1,800;1,900&family=Montserrat:wght@500;600&display=swap">
<style>
:root{
  --backdrop:#e2e2e2;
  --page-blue:#2e3aa6;
  --page-blue-deep:#25308f;
  --glow-yellow:#d8d41e;
  --band-ink:#1f2570;
  --soft-white:#e4e4ea;
  --photo-a:#3a2a9a;
  --photo-b:#6a2fb0;
  --photo-c:#1f5fc4;
}
*{margin:0;padding:0;box-sizing:border-box}
html,body{width:1200px;height:886px;overflow:hidden;background:var(--backdrop)}
body{position:relative;font-family:"Montserrat",sans-serif}
.page{position:absolute;width:452px;height:319px;overflow:hidden;
  background:radial-gradient(circle at 70% 40%,#3443b4 0%,var(--page-blue) 55%,var(--page-blue-deep) 100%);
  box-shadow:0 10px 18px rgba(0,0,0,.25)}
.page--cover{left:105px;top:81px}
.page--terms{left:632px;top:81px}
.page--policy{left:105px;top:464px}
.page--packages{left:632px;top:464px}
.photo-panel{position:absolute;left:0;top:0;width:452px;height:319px}
.txt{position:absolute;color:var(--glow-yellow)}
.headline{font-family:"Exo 2",sans-serif;font-style:italic;font-weight:900}
.band{position:absolute;background:var(--glow-yellow);transform:skewX(-14deg)}
.band span{display:block;transform:skewX(14deg);font-family:"Exo 2",sans-serif;font-style:italic;font-weight:800;color:var(--band-ink)}
.tick{position:absolute;display:flex;align-items:flex-start;gap:4px;color:var(--soft-white);font-size:6.3px;font-weight:600;line-height:1.2;text-transform:uppercase}
.tick svg{flex:none;width:11px;height:11px;margin-top:-2px}
.brand{position:absolute;right:17px;top:12px;font-family:"Montserrat",sans-serif;font-weight:600;font-size:13px;color:var(--soft-white);letter-spacing:1px;text-transform:uppercase}
.hero-3d{left:251px;top:44px;font-size:98px;line-height:1;letter-spacing:-4px}
.hero-3d .three{color:var(--soft-white)}
.hero-3d .dee{color:var(--glow-yellow)}
.hero-sub{left:252px;top:136px;font-size:25px;color:var(--soft-white)}
.para{position:absolute;color:var(--glow-yellow);text-align:justify}
.note-title{left:159px;top:83px;font-size:11px;color:var(--soft-white)}
.price{font-size:29px;line-height:1}
.per{font-size:9px;color:var(--soft-white)}
</style>
</head>
<body>

<!-- Page 1 : cover -->
<section class="page page--cover">
  <svg class="photo-panel" viewBox="0 0 452 319">
    <defs><linearGradient id="g1" x1="0" y1="0" x2="1" y2="1"><stop offset="0" stop-color="var(--photo-a)"/><stop offset=".5" stop-color="var(--photo-c)"/><stop offset="1" stop-color="var(--photo-b)"/></linearGradient></defs>
    <polygon points="0,0 169,0 238,158 169,319 0,319" fill="url(#g1)" role="img" aria-label="Photo of players putting in front of a glowing painted mural"/>
    <polyline points="169,0 238,158 169,319" fill="none" stroke="var(--glow-yellow)" stroke-width="3"/>
  </svg>
  <div class="brand">Lumen Burrow</div>
  <div class="txt headline hero-3d"><span class="three">3</span><span class="dee">D</span></div>
  <div class="txt headline hero-sub">MINI GOLF</div>
  <div class="band" style="left:226px;top:165px;width:208px;height:46px;padding:8px 0 0 6px">
    <span style="font-size:11.5px;line-height:13px">3D MINI GOLF GROUP BOOKINGS<br>OF 15 PEOPLE, WE OFFER</span>
  </div>
  <div class="tick" style="left:238px;top:225px"><svg viewBox="0 0 12 12"><circle cx="6" cy="6" r="5" fill="none" stroke="var(--glow-yellow)" stroke-width="1.2"/><path d="M3 6l2.2 2.2L11 1.5" fill="none" stroke="var(--glow-yellow)" stroke-width="1.6"/></svg>Adults 16+yrs - $25pp (discounted rate)</div>
  <div class="tick" style="left:238px;top:245px"><svg viewBox="0 0 12 12"><circle cx="6" cy="6" r="5" fill="none" stroke="var(--glow-yellow)" stroke-width="1.2"/><path d="M3 6l2.2 2.2L11 1.5" fill="none" stroke="var(--glow-yellow)" stroke-width="1.6"/></svg>Concession - $16.50pp (discounted rate).<br>Accepted concessions are:<br>Federal pensioners, WA seniors card<br>holders and disability pensioners</div>
</section>

<!-- Page 2 : terms -->
<section class="page page--terms">
  <svg class="photo-panel" viewBox="0 0 452 319">
    <defs><linearGradient id="g2" x1="0" y1="0" x2="1" y2="1"><stop offset="0" stop-color="var(--photo-b)"/><stop offset=".6" stop-color="var(--photo-a)"/><stop offset="1" stop-color="#1d1a6a"/></linearGradient></defs>
    <polygon points="0,0 82,0 152,155 82,319 0,319" fill="url(#g2)" role="img" aria-label="Photo of a player in 3D glasses putting under glowing artwork"/>
    <polyline points="82,0 152,155 82,319" fill="none" stroke="var(--glow-yellow)" stroke-width="3"/>
  </svg>
  <div class="band" style="left:92px;top:17px;width:342px;height:31px;padding:2px 0 0 68px">
    <span style="font-size:9px;line-height:13px">IF NUMBERS DROP BELOW 15 PEOPLE 7 DAYS BEFORE<br>BOOKING STANDARD PRICING APPLIES</span>
  </div>
  <div class="tick" style="left:172px;top:61px"><svg viewBox="0 0 12 12"><circle cx="6" cy="6" r="5" fill="none" stroke="var(--glow-yellow)" stroke-width="1.2"/><path d="M3 6l2.2 2.2L11 1.5" fill="none" stroke="var(--glow-yellow)" stroke-width="1.6"/></svg>Adults - $25pp</div>
  <div class="tick" style="left:262px;top:61px"><svg viewBox="0 0 12 12"><circle cx="6" cy="6" r="5" fill="none" stroke="var(--glow-yellow)" stroke-width="1.2"/><path d="M3 6l2.2 2.2L11 1.5" fill="none" stroke="var(--glow-yellow)" stroke-width="1.6"/></svg>Concession - $16.50pp</div>
  <div class="txt headline note-title">NOTE</div>
  <p class="para" style="left:159px;top:94px;width:275px;font-size:6.1px;line-height:8.6px;font-weight:500">Bookings for 14 people or less must be made via our booking website. Full payment is required to secure the booking. To book for more than 11 people (e.g., 14) 2 bookings are required. Just book in 11 people for 1 timeslot let's say 4:00 PM and the other 3 people for the timeslot after that, so 4:15 PM. Please let everyone know to arrive 10 minutes before the first booked timeslot. That way you will not be separated in the golf rooms.</p>
  <div class="band" style="left:150px;top:154px;width:284px;height:30px;padding:2px 0 0 10px">
    <span style="font-size:9px;line-height:13px">WE REQUIRE A DEPOSIT TO SECURE YOUR BOOKING, WHICH<br>IS NON REFUNDABLE 7 DAYS BEFORE THE BOOKING</span>
  </div>
  <div class="tick" style="left:172px;top:199px"><svg viewBox="0 0 12 12"><circle cx="6" cy="6" r="5" fill="none" stroke="var(--glow-yellow)" stroke-width="1.2"/><path d="M3 6l2.2 2.2L11 1.5" fill="none" stroke="var(--glow-yellow)" stroke-width="1.6"/></svg>Groups of 15-25 people<br>- $100 deposit</div>
  <div class="tick" style="left:296px;top:199px"><svg viewBox="0 0 12 12"><circle cx="6" cy="6" r="5" fill="none" stroke="var(--glow-yellow)" stroke-width="1.2"/><path d="M3 6l2.2 2.2L11 1.5" fill="none" stroke="var(--glow-yellow)" stroke-width="1.6"/></svg>Groups of 25+ people<br>– 20% of overall costing</div>
  <p class="para" style="left:159px;top:224px;width:275px;font-size:8px;line-height:10.5px;font-weight:500">Full Payment for group bookings are required 3 days before your event and is non-refundable</p>
  <p class="para" style="left:159px;top:258px;width:275px;font-size:6.1px;line-height:8.6px;font-weight:500">We are not licensed but BYO is allowed at the venue. It is a $5 corkage fee per person and limited to strictly 2 standard pre-packaged drinks per person. Pre-packaged is defined as something you can drink from directly, such as cans or bottles of beer. Sharing drinks (e.g., bottles wine) is not permitted as they are easily spilled. Please note that we are unable to keep your drinks cold due to limited fridge space.</p>
</section>

<!-- Page 3 : booking policy -->
<section class="page page--policy">
  <svg class="photo-panel" viewBox="0 0 452 319">
    <defs><linearGradient id="g3" x1="0" y1="0" x2="0" y2="1"><stop offset="0" stop-color="#2a2f8e"/><stop offset=".55" stop-color="var(--photo-a)"/><stop offset=".8" stop-color="#5a3fa0"/><stop offset="1" stop-color="#a86a6a"/></linearGradient></defs>
    <polygon points="0,0 83,0 152,164 83,319 0,319" fill="url(#g3)" role="img" aria-label="Photo of a golf room with a space-themed mural and timber floor"/>
    <polyline points="83,0 152,164 83,319" fill="none" stroke="var(--glow-yellow)" stroke-width="3"/>
  </svg>
  <div class="para" style="left:159px;top:18px;width:275px;font-size:8.2px;line-height:10.7px;font-weight:500">
    <p>When making a booking we need you to confirm how many people will be attending 7 days before the event. This confirmation of numbers will represent the final total to be invoiced, as per our ticket pricing. Your booking will then be updated in our booking calendar to reflect the final numbers and accordingly your spots are reserved and not available to other customers.</p>
    <p style="margin-top:10px">If the number of attendees has dropped to less than 15 people 7 days before the booking it is not considered a group booking anymore and we require full payment for the booking.</p>
    <p style="margin-top:10px">If the number of attendees has dropped to less than 15 people 7 days before the booking it is not considered a group booking anymore and we require full payment for the booking.</p>
    <p style="margin-top:10px">Children under 5 years of age are NOT allowed in the golf rooms for safety reasons unless they stay secured in a pram or carrier at all times.</p>
    <p style="margin-top:12px">For group bookings of 15+ players, we can open the venue outside of our trading hours!</p>
    <p style="margin-top:12px">We also offer Party Packages that come with Private Room hire, Decoration, Music and Food. Please follow the link to find out more. You need a minimum of 12 People for the Party package</p>
  </div>
</section>

<!-- Page 4 : catered packages -->
<section class="page page--packages">
  <svg class="photo-panel" viewBox="0 0 452 319">
    <defs><linearGradient id="g4" x1="0" y1="0" x2="1" y2="1"><stop offset="0" stop-color="#1f8a6a"/><stop offset=".4" stop-color="var(--photo-c)"/><stop offset="1" stop-color="var(--photo-a)"/></linearGradient></defs>
    <polygon points="0,0 82,0 155,158 82,319 0,319" fill="url(#g4)" role="img" aria-label="Photo of a team in 3D glasses holding putters under glowing murals"/>
    <polyline points="82,0 155,158 82,319" fill="none" stroke="var(--glow-yellow)" stroke-width="3"/>
  </svg>
  <div class="txt headline" style="left:147px;top:13px;font-size:14px">OUR CATERED TEAM</div>
  <div class="txt headline" style="left:146px;top:24px;font-size:30px;line-height:28px">BUILDING<br>PACKAGES</div>

  <div class="band" style="left:126px;top:90px;width:160px;height:18px;padding:2px 0 0 38px"><span style="font-size:9px">SNACK PACKAGE</span></div>
  <div class="txt headline price" style="left:294px;top:85px">$40</div>
  <div class="txt headline per" style="left:355px;top:94px">PER PERSON</div>
  <div class="tick" style="left:168px;top:124px"><svg viewBox="0 0 12 12"><circle cx="6" cy="6" r="5" fill="none" stroke="var(--glow-yellow)" stroke-width="1.2"/><path d="M3 6l2.2 2.2L11 1.5" fill="none" stroke="var(--glow-yellow)" stroke-width="1.6"/></svg>2 Mini sausage rolls</div>
  <div class="tick" style="left:291px;top:124px"><svg viewBox="0 0 12 12"><circle cx="6" cy="6" r="5" fill="none" stroke="var(--glow-yellow)" stroke-width="1.2"/><path d="M3 6l2.2 2.2L11 1.5" fill="none" stroke="var(--glow-yellow)" stroke-width="1.6"/></svg>2 Mini party pies</div>
  <div class="tick" style="left:168px;top:144px"><svg viewBox="0 0 12 12"><circle cx="6" cy="6" r="5" fill="none" stroke="var(--glow-yellow)" stroke-width="1.2"/><path d="M3 6l2.2 2.2L11 1.5" fill="none" stroke="var(--glow-yellow)" stroke-width="1.6"/></svg>Potato gems</div>
  <div class="tick" style="left:291px;top:144px"><svg viewBox="0 0 12 12"><circle cx="6" cy="6" r="5" fill="none" stroke="var(--glow-yellow)" stroke-width="1.2"/><path d="M3 6l2.2 2.2L11 1.5" fill="none" stroke="var(--glow-yellow)" stroke-width="1.6"/></svg>Spring rolls</div>
  <div class="tick" style="left:168px;top:165px"><svg viewBox="0 0 12 12"><circle cx="6" cy="6" r="5" fill="none" stroke="var(--glow-yellow)" stroke-width="1.2"/><path d="M3 6l2.2 2.2L11 1.5" fill="none" stroke="var(--glow-yellow)" stroke-width="1.6"/></svg>1 Soft drink and water</div>

  <div class="band" style="left:138px;top:184px;width:148px;height:18px;padding:2px 0 0 26px"><span style="font-size:9px">ALL INCLUSIVE PACKAGE</span></div>
  <div class="txt headline price" style="left:294px;top:179px">$55</div>
  <div class="txt headline per" style="left:355px;top:188px">PER PERSON</div>
  <div class="tick" style="left:168px;top:219px"><svg viewBox="0 0 12 12"><circle cx="6" cy="6" r="5" fill="none" stroke="var(--glow-yellow)" stroke-width="1.2"/><path d="M3 6l2.2 2.2L11 1.5" fill="none" stroke="var(--glow-yellow)" stroke-width="1.6"/></svg>Mini sausage rolls</div>
  <div class="tick" style="left:290px;top:219px"><svg viewBox="0 0 12 12"><circle cx="6" cy="6" r="5" fill="none" stroke="var(--glow-yellow)" stroke-width="1.2"/><path d="M3 6l2.2 2.2L11 1.5" fill="none" stroke="var(--glow-yellow)" stroke-width="1.6"/></svg>Spinach and ricotta pastries</div>
  <div class="tick" style="left:168px;top:240px"><svg viewBox="0 0 12 12"><circle cx="6" cy="6" r="5" fill="none" stroke="var(--glow-yellow)" stroke-width="1.2"/><path d="M3 6l2.2 2.2L11 1.5" fill="none" stroke="var(--glow-yellow)" stroke-width="1.6"/></svg>Dumplings</div>
  <div class="tick" style="left:290px;top:240px"><svg viewBox="0 0 12 12"><circle cx="6" cy="6" r="5" fill="none" stroke="var(--glow-yellow)" stroke-width="1.2"/><path d="M3 6l2.2 2.2L11 1.5" fill="none" stroke="var(--glow-yellow)" stroke-width="1.6"/></svg>Spring rolls</div>
  <div class="tick" style="left:168px;top:260px"><svg viewBox="0 0 12 12"><circle cx="6" cy="6" r="5" fill="none" stroke="var(--glow-yellow)" stroke-width="1.2"/><path d="M3 6l2.2 2.2L11 1.5" fill="none" stroke="var(--glow-yellow)" stroke-width="1.6"/></svg>Sweet potato chips</div>
  <div class="tick" style="left:290px;top:260px"><svg viewBox="0 0 12 12"><circle cx="6" cy="6" r="5" fill="none" stroke="var(--glow-yellow)" stroke-width="1.2"/><path d="M3 6l2.2 2.2L11 1.5" fill="none" stroke="var(--glow-yellow)" stroke-width="1.6"/></svg>Sauce for dip</div>
  <div class="tick" style="left:168px;top:280px"><svg viewBox="0 0 12 12"><circle cx="6" cy="6" r="5" fill="none" stroke="var(--glow-yellow)" stroke-width="1.2"/><path d="M3 6l2.2 2.2L11 1.5" fill="none" stroke="var(--glow-yellow)" stroke-width="1.6"/></svg>1 Soft drink and water</div>
  <div class="tick" style="left:290px;top:280px"><svg viewBox="0 0 12 12"><circle cx="6" cy="6" r="5" fill="none" stroke="var(--glow-yellow)" stroke-width="1.2"/><path d="M3 6l2.2 2.2L11 1.5" fill="none" stroke="var(--glow-yellow)" stroke-width="1.6"/></svg>Corkage included for BYO,<br>subject to 2 standard drinks<br>inside the golf rooms<br>(normally $5pp)</div>
</section>

</body>
</html>
```